CD-Design für aufstrebende Newcomer Band
Zielgruppe
Wir sind eine Band (2 Brüder/ 20 und 23 Jahre alt) die ihre Debut-EP veröffentlichen.
Zielgruppe ist eher weiblich und jung (25 und jünger).
Die Band ist im Genre Pop / Singer-Songwriter.
http://www.funkenpaar-musik.de/
Songs sind in diesem Stil:
https://www.klangfilmportal.de/watch?v=Rb7tKm2Lq9x
https://www.klangfilmportal.de/watch?v=Hn4wXe8Pz3d
https://www.klangfilmportal.de/watch?v=Gs2vYc6Nj5t
Aufgabenstellung
Gesucht wird Design für CD + Cover + Inlay + Rückseite
Werbung des Designers im Inlay möglich.
Alle Dateien von uns (Logo, Fotos, Songtexte) können hier gefunden werden:
https://www.ablagekiste-online.de/sh/k3rw8m1tq52xb7z/BBQxLp4Fn2HeR_7TzmWk9aJd?dl=0
Die EP heißt: Nordlicht
Bitte unsere Gesichter gut platzieren (ist unsere erste CD und Fans sollen uns sofort wiedererkennen bzw unsere Gesichter als Marke positionieren)
Thema muss nicht unbedingt auf 'Nordlicht' gestützt sein.
Bitte die Schrift nicht in diesem Style, wie diese Sendung:
http://www.talfunk-sender.de/programm/sendungen/s-z/Sternwind_logo100~_v-box__16__9_-c41e7b2f90da63d85e1a2b47c9f0e13a6d8b5c27.png
Folgende Songs sind auf der EP (Rückseite):
1. Regen-Glanz
2. Wellen
3. Still Gehen
4. Spiegel
5. Nordlicht
6. Funken
7. Ihr
8. Regen-Glanz (Akustik)
9. Nordlicht (Akustik)
10. Nordlicht (Lindhalt Remix)
Produziert von T.B.Klangwerkstatt

```html
<!DOCTYPE html>
<html lang="de">
<head>
<meta charset="utf-8">
<title>Funkenpaar – Nordlicht EP</title>
<link href="https://fonts.googleapis.com/css2?family=Roboto:wght@300;500;700&display=swap" rel="stylesheet">
<style>
  :root {
    --canvas: #ffffff;
    --ink-light: #ffffff;
    --cover-dark: #1c1c1c;
    --cover-mid: #3a3a3a;
    --back-dark: #2e2e2e;
    --back-mid: #4a4a4a;
    --disc: #222222;
    --shadow: rgba(0,0,0,0.25);
  }
  * { margin: 0; padding: 0; box-sizing: border-box; }
  html, body {
    width: 1200px; height: 1046px; overflow: hidden;
    background: var(--canvas);
    font-family: "Roboto", Arial, sans-serif;
  }
  .sheet { position: relative; width: 1200px; height: 1046px; }

  .panel {
    position: absolute; width: 434px; height: 435px;
    box-shadow: 0 1px 4px var(--shadow);
    overflow: hidden; color: var(--ink-light);
  }
  .front-cover { left: 202px; top: 91px; }
  .back-cover  { left: 202px; top: 560px; }

  .photo { position: absolute; inset: 0; }
  .front-cover .photo {
    background: radial-gradient(ellipse at 50% 60%, var(--cover-mid) 0%, var(--cover-dark) 75%);
  }
  .back-cover .photo {
    background: linear-gradient(90deg, var(--back-dark) 0%, var(--back-mid) 55%, var(--back-dark) 100%);
  }

  .title-grid {
    position: absolute; left: 0; top: 0; width: 100%; height: 100%;
  }
  .title-grid span {
    position: absolute; width: 60px; margin-left: -30px;
    text-align: center; font-weight: 300; font-size: 56px; line-height: 1;
  }
  .title-grid .marked {
    color: var(--cover-dark);
  }
  .title-grid .marked::before {
    content: ""; position: absolute; left: 50%; top: 50%;
    width: 54px; height: 54px; margin: -27px 0 0 -27px;
    border-radius: 50%; background: var(--ink-light); z-index: -1;
  }
  .title-grid .marked { z-index: 1; isolation: isolate; }

  .band-name {
    position: absolute; left: 0; width: 100%; text-align: center;
    font-weight: 300; font-size: 15px; letter-spacing: 2px;
  }
  .front-cover .band-name { top: 398px; }
  .back-cover .band-name { top: 396px; }

  .tracklist {
    position: absolute; left: 0; top: 22px; width: 100%;
    list-style: none; text-align: center;
  }
  .tracklist li { height: 27.4px; }
  .track-no { display: block; font-size: 6px; font-weight: 700; line-height: 8px; }
  .track-title {
    display: block; font-size: 10.5px; font-weight: 500; letter-spacing: 1.6px; line-height: 13px;
  }
  .track-note { font-size: 5.5px; font-weight: 700; letter-spacing: 0.6px; margin-left: 3px; }

  .credit {
    position: absolute; left: 0; top: 320px; width: 100%; text-align: center;
    font-size: 5.5px; font-weight: 700; letter-spacing: 0.8px;
  }

  .disc { position: absolute; left: 696px; top: 99px; width: 418px; height: 418px; }
</style>
</head>
<body>
<main class="sheet">

  <section class="panel front-cover">
    <div class="photo" role="img" aria-label="Schwarzweißfoto der beiden Bandmitglieder, sitzend mit Zeitung und Akustikgitarre"></div>
    <div class="title-grid" aria-label="Nordlicht">
      <span style="left:141px;top:128px">N</span>
      <span style="left:215px;top:128px">O</span>
      <span style="left:289px;top:128px">R</span>
      <span style="left:141px;top:188px">D</span>
      <span class="marked" style="left:215px;top:188px">L</span>
      <span style="left:289px;top:188px">I</span>
      <span style="left:141px;top:248px">C</span>
      <span style="left:215px;top:248px">H</span>
      <span style="left:289px;top:248px">T</span>
    </div>
    <p class="band-name">FUNKENPAAR</p>
  </section>

  <svg class="disc" viewBox="0 0 418 418" aria-label="CD-Aufdruck Nordlicht">
    <defs>
      <path id="rim-path" d="M 209 209 m 0 -192 a 192 192 0 1 1 0 384 a 192 192 0 1 1 0 -384" />
    </defs>
    <circle cx="209" cy="209" r="209" fill="var(--disc)"/>
    <circle cx="209" cy="213" r="28" fill="var(--canvas)"/>
    <g fill="var(--ink-light)" font-family="Roboto, Arial, sans-serif" font-weight="300" font-size="56" text-anchor="middle">
      <text x="140" y="175">N</text><text x="209" y="175">O</text><text x="273" y="175">R</text>
      <text x="140" y="233">D</text><text x="273" y="233">I</text>
      <text x="140" y="291">C</text><text x="209" y="291">H</text><text x="273" y="291">T</text>
    </g>
    <text x="209" y="350" fill="var(--ink-light)" font-family="Roboto, Arial, sans-serif" font-weight="300" font-size="15" letter-spacing="2" text-anchor="middle">FUNKENPAAR</text>
    <text fill="var(--ink-light)" font-family="Roboto, Arial, sans-serif" font-weight="700" font-size="5.5" letter-spacing="0.8">
      <textPath href="#rim-path" startOffset="10%">PRODUZIERT VON T.B.KLANGWERKSTATT</textPath>
    </text>
  </svg>

  <section class="panel back-cover">
    <div class="photo" role="img" aria-label="Schwarzweißfoto der Band: ein Mitglied an der Wand lehnend, vorne ein zweites mit Akustikgitarre"></div>
    <ol class="tracklist">
      <li><span class="track-no">1</span><span class="track-title">REGEN-GLANZ</span></li>
      <li><span class="track-no">2</span><span class="track-title">WELLEN</span></li>
      <li><span class="track-no">3</span><span class="track-title">STILL GEHEN</span></li>
      <li><span class="track-no">4</span><span class="track-title">SPIEGEL</span></li>
      <li><span class="track-no">5</span><span class="track-title">NORDLICHT</span></li>
      <li><span class="track-no">6</span><span class="track-title">FUNKEN</span></li>
      <li><span class="track-no">7</span><span class="track-title">IHR</span></li>
      <li><span class="track-no">8</span><span class="track-title">REGEN-GLANZ<span class="track-note">(AKUSTIK)</span></span></li>
      <li><span class="track-no">9</span><span class="track-title">NORDLICHT<span class="track-note">(AKUSTIK)</span></span></li>
      <li><span class="track-no">10</span><span class="track-title">NORDLICHT<span class="track-note">(LINDHALT REMIX)</span></span></li>
    </ol>
    <p class="credit">PRODUZIERT VON T.B.KLANGWERKSTATT</p>
    <p class="band-name">FUNKENPAAR</p>
  </section>

</main>
</body>
</html>
```